Simple and clean poster/flyer design needed for public speaker!

SIMPLE AND CLEAN DESIGN NEEDED FOR POSTER/FLYER

I AM a public speaker based in London (www.tobiaskernwald.com)
and I would like to have a custom-made flyer/poster
(preferably in adobe CS4 template format) that I con customize (just changing the text) for my various speeches, topics and locations

I am looking for something very simple and clean.
NO extravagance or crowded poster, but a rather beautiful clean and eye-catching design that clearly informs people what i am talking about, where and when.

Go to my website www.tobiaskernwald.com
to see the colour scheme and style that I like
my poster should be like the website, similar colours, logo, clean, simple and clear.

Summary

(1) simple and clean design
(2) design that fits my brand (see website)
(3) clear and eye-catching to promote my speeches
(4) customizable for my various talks, by simply chancing the text (Please Adobe Photoshop CS4 template format)
(5)in A3, A4, A5, A6 sizes, so i can use it for both flyers and small posters

ADDITIONS

BIG BOLD HEADLINE TO GRAP ATTENTION, greatest prominence

sub headline to explain, smaller than the headline, but still prominent on the poster

just a few bullet points to list the benefits and answer the “whats in for me”-question
this is for people who are already interested and continue reading, medium prominence.

WHERE, WHEN, HOW MUCH-information, in the lower section of the poster, little text, but clearly visible

only one point of CONTACT on my poster “www.tobiaskernwald.com”, bit big and clear so that it is very prominent

little text, effectively used
LESS IS MORE
Updates

contact me regarding logo files and any questions you may have!

for the logo files go to

https://secure.dropvaultly.com/fs/v.aspx?v=41958b2d703c9ea1f6d2

click on the folder "logo pack" to see the files

eps
jpg
png
photoshop
TIF

thanks for your interest. hope to see great designs!
I am really looking forward to it
if you have any questions, please do not hesitate to ask

Kind Regards
Tobias
 

• Simple, clean design, text sparingly used.

• The mood should be light-hearted, calm, bright, simple and friendly, comic like

• a lot of white space, calling more attention to the content

• a light blue, dark blue, white and black colour scheme as seen on the homepage (www.tobiaskernwald.com) please use the exact same colours as seen on the homepage.

White being most predominant, 2 different blue used to highlight something, black for text on white background.

• One graphic would be cool, as long as it is blue. It could be waves-like graphic, or something like the white pattern in the background, in my case just in blue on white background > http://www.lumenquietharbor.org/., I do not mean exactly this graphic and not that crowded but a simple single graphic in blue as long as it fits the theme and feel of my poster

Top o f the poster

• (a )One short bold headline (TALK TITLE) with a sub-headline below it (hook)

• or (b) headline as question (…....?) and below sub-headline offering the solution (my talk ;-) of course)

• 3 benefits as on homepage, that I can adapt for each talk (bottom right of my start site “what are you looking for?” either blue on white, or as in the page white on blue...whatever looks better and fits the design). Not sure how that looks, and if to include it!

• the bottom of the poster will have “Where”-information “when”-information “ticket price” info

• contact at the very bottom...for more into or to purchase tickets (my website and email)

If you have any questions or need clarification please write me!

Requirements
Must have
• lot of white space
• less is more - simple design
• little text, little graphics- only used when necessary to greatest effect.
• light, friendly, modern feel
• blue-color scheme

```html
<!DOCTYPE html>
<html lang="en">
<head>
<meta charset="utf-8">
<title>Is Life Happening To Me – Talk Poster</title>
<link rel="stylesheet" href="https://fonts.googleapis.com/css2?family=Arimo:wght@400;700&family=PT+Sans:wght@700&display=swap">
<style>
  :root {
    --sky-deep: #6aaac8;
    --sky-mid: #8cc3da;
    --sky-light: #a6d3e4;
    --mist: #e3f0f5;
    --mist-light: #f1f8fb;
    --label-blue: #5fa3c2;
    --brand-blue: #3aa2d8;
    --rim-blue: #6ea9c5;
    --white: #ffffff;
    --ink: #111111;
    --ink-soft: #3a3a3a;
  }
  * { margin: 0; padding: 0; box-sizing: border-box; }
  html, body { width: 849px; height: 1200px; overflow: hidden; }
  body { font-family: "Arimo", Arial, sans-serif; background: var(--mist); }

  .poster {
    position: relative;
    width: 849px;
    height: 1200px;
    overflow: hidden;
    background: linear-gradient(180deg, var(--mist) 0%, #e8f3f7 100%);
  }

  .sky {
    position: absolute;
    left: 0; top: 0;
    width: 849px; height: 830px;
    background: radial-gradient(ellipse 520px 520px at 455px 460px, var(--sky-light) 0%, var(--sky-mid) 55%, var(--sky-deep) 100%);
  }

  .question-mark {
    position: absolute;
    right: -14px;
    top: -92px;
    font-size: 330px;
    line-height: 1;
    font-weight: 700;
    color: rgba(255,255,255,0.9);
  }

  .headline {
    position: absolute;
    left: 116px;
    top: 150px;
    font-size: 54px;
    line-height: 54px;
    font-weight: 700;
    color: var(--white);
    letter-spacing: -0.3px;
    text-shadow: 0 2px 3px rgba(60,110,140,0.25);
    white-space: nowrap;
  }

  .subheadline {
    position: absolute;
    left: 273px;
    top: 226px;
    font-size: 30px;
    line-height: 30px;
    font-weight: 700;
    color: var(--white);
    white-space: nowrap;
  }

  .benefits-title {
    position: absolute;
    left: 123px;
    top: 336px;
    font-size: 29px;
    line-height: 29px;
    font-weight: 700;
    color: var(--white);
  }

  .benefits {
    position: absolute;
    left: 272px;
    top: 391px;
    list-style: none;
  }
  .benefits li {
    width: 28px; height: 28px;
    border-radius: 50%;
    margin-bottom: 36px;
    background: radial-gradient(circle at 45% 40%, #ffffff 0%, #eef7fb 60%, #d6eaf2 100%);
  }

  .info-bubble {
    position: absolute;
    left: 0; top: 0;
    width: 849px; height: 1200px;
  }

  .vine {
    position: absolute;
    left: 416px;
    top: 713px;
    width: 330px;
    height: 400px;
    border-radius: 40% 60% 30% 70%;
    background: radial-gradient(ellipse at 50% 45%, rgba(255,255,255,0.35) 0%, rgba(255,255,255,0) 70%);
  }

  .details {
    position: absolute;
    left: 0;
    top: 771px;
    width: 849px;
  }
  .details .row {
    display: flex;
    height: 31px;
    align-items: baseline;
  }
  .details dt {
    width: 430px;
    text-align: right;
    font-size: 24px;
    line-height: 31px;
    color: var(--label-blue);
  }
  .details dd {
    padding-left: 11px;
    font-size: 24px;
    line-height: 31px;
    color: var(--ink-soft);
  }

  .brand {
    position: absolute;
    left: 98px;
    top: 1060px;
    display: flex;
    align-items: flex-end;
  }
  .brand-dot {
    width: 56px; height: 56px;
    border-radius: 50%;
    background: var(--brand-blue);
    margin-right: 24px;
    margin-bottom: 12px;
  }
  .brand-name {
    font-size: 25px;
    line-height: 25px;
    font-weight: 400;
    color: var(--brand-blue);
    letter-spacing: -0.3px;
  }
  .brand-role {
    font-size: 15px;
    line-height: 18px;
    color: var(--ink-soft);
    letter-spacing: 0.2px;
  }

  .slogan {
    position: absolute;
    left: 551px;
    top: 1110px;
    font-family: "PT Sans", Arial, sans-serif;
    font-size: 52px;
    line-height: 52px;
    font-weight: 700;
    color: var(--ink);
    letter-spacing: -2.4px;
    white-space: nowrap;
  }
</style>
</head>
<body>
  <main class="poster">
    <div class="sky"></div>
    <div class="question-mark" aria-hidden="true">?</div>

    <h1 class="headline">Is Life Happening To Me</h1>
    <p class="subheadline">A detail talk on meaning of life..</p>

    <h2 class="benefits-title">what’s in for me?</h2>
    <ul class="benefits" aria-label="Benefits">
      <li></li>
      <li></li>
      <li></li>
    </ul>

    <svg class="info-bubble" viewBox="0 0 849 1200" width="849" height="1200" aria-hidden="true">
      <defs>
        <linearGradient id="bubbleFill" x1="0" y1="0" x2="0" y2="1">
          <stop offset="0" stop-color="#eef7fb"/>
          <stop offset="1" stop-color="#e2f0f6"/>
        </linearGradient>
      </defs>
      <path d="M64 758 H785 A64 71 0 0 1 849 829 A64 71 0 0 1 785 900 H462 Q438 903 427 951 Q416 903 392 900 H64 A64 71 0 0 1 0 829 A64 71 0 0 1 64 758 Z"
            fill="url(#bubbleFill)" stroke="rgba(255,255,255,0.8)" stroke-width="1.5"/>
      <path d="M1 840 A64 62 0 0 0 64 900 H392 Q416 903 427 951 Q438 903 462 900 H785 A64 62 0 0 0 848 840"
            fill="none" stroke="var(--rim-blue)" stroke-width="3"/>
    </svg>

    <div class="vine" role="img" aria-label="Faint white vine with leaves curling around the info panel"></div>

    <dl class="details">
      <div class="row"><dt>where:</dt><dd></dd></div>
      <div class="row"><dt>when:</dt><dd></dd></div>
      <div class="row"><dt>get your ticket :</dt><dd></dd></div>
      <div class="row"><dt>contact:</dt><dd>www.tobiaskernwald.com</dd></div>
    </dl>

    <div class="brand">
      <span class="brand-dot" aria-hidden="true"></span>
      <div class="brand-text">
        <div class="brand-name">TOBIAS KERNWALD</div>
        <div class="brand-role">SPRITUAL SPEAKER</div>
      </div>
    </div>

    <p class="slogan">Less is more.</p>
  </main>
</body>
</html>
```